Business Card for Luxury Hospitality Industry Career Seeker

Need something Simple, Punctual, and Elegant.

Project goal is to update phone number, layout, and wording

I look forward to working with you to create a business card I can give to managers and employers in the Luxury Hospitality industry. I want to advance a career in this industry handing out cards to managers and directors on my way up.
Updates

Updated graphics preferences in brief - would like my name flanked by small Lion, Compass, & Rope and have the Halworth 5 Star logo on the back Added Saturday, January 14, 2017

Updated Brief:-Some wording has been removed-Card Front should be more simple and tidy now-Card Back word choice & flow is improved Added Sunday, January 15, 2017

Target Market(s)

Luxury Hospitality Industry Employers and Managers

Industry/Entity Type

Hospitality

Contact Information for Business Card

(Card Front)
Corbin T. Pellman (flanked by small Lion, Compass & Rope graphic)
Luxury Hospitality
555-317-8846
ridgefellow@mailvessel.example
netroster.example/in/corbin-pellman-vet-civ
My Experience = Our Success

(Card Back)
Graphic of: Halworth 5 Star logo and maybe QTR 5 Diamond Logo too
8 years military supply, logistics, & administrative experience
2 years intensive recruiting, marketing, and sales expertise
Adept problem solving, planning and management skills
5 Star, 5 Daimond, Luxury Hotels & Hospitality Rooms & Revenue

Requirements
Must have
• Name
• Phone Number
• Email Address
• Net Roster Address
• Slogan (My Experience = Our Success)
• Graphic on back: Halworth 5 Star logo
• Qualification Remarks
• Catchy logo
Nice to have
• Background that makes a viewer think Luxury Hospitality Experience and/or World Experience
• Color combinations I've seen & liked are black & yellow, black & white, and blue & white

```html
<!DOCTYPE html>
<html lang="en">
<head>
<meta charset="utf-8">
<title>Corbin T. Pellman – Luxury Hospitality Business Card</title>
<link rel="stylesheet" href="https://fonts.googleapis.com/css2?family=PT+Sans:wght@400;700&family=Tinos:wght@700&display=swap">
<style>
  :root {
    --page-bg: #d6d6d4;
    --card-black: #050505;
    --card-edge: #1a1a1a;
    --gold: #f0c419;
    --gold-deep: #c99a12;
    --gold-muted: #b59b32;
    --sans: "PT Sans", Arial, sans-serif;
    --serif: "Tinos", "Times New Roman", serif;
  }
  * { margin: 0; padding: 0; box-sizing: border-box; }
  html, body {
    width: 1200px;
    height: 900px;
    overflow: hidden;
    background: var(--page-bg);
  }
  .canvas {
    position: relative;
    width: 1200px;
    height: 900px;
  }
  .card {
    position: absolute;
    width: 480px;
    height: 290px;
    background: var(--card-black);
    border: 1px solid var(--card-edge);
    border-radius: 12px;
    box-shadow: 0 6px 16px rgba(0,0,0,0.35);
    overflow: hidden;
    font-family: var(--sans);
    color: var(--gold);
  }

  /* Card back: qualifications */
  .card-back { left: 170px; top: 140px; }
  .rule {
    position: absolute;
    height: 3px;
    background: var(--gold);
  }
  .card-back .rule-top { left: 38px; right: 38px; top: 40px; }
  .card-back .rule-bottom { left: 38px; right: 38px; top: 152px; }
  .qualifications {
    position: absolute;
    left: 40px;
    right: 30px;
    top: 52px;
    list-style: none;
  }
  .qualifications li {
    display: flex;
    align-items: center;
    gap: 6px;
    font-size: 12.6px;
    line-height: 22px;
    white-space: nowrap;
  }
  .tick { width: 13px; height: 13px; flex: none; }
  .hotel-crest {
    position: absolute;
    left: 165px;
    top: 160px;
    width: 150px;
    height: 112px;
    border-radius: 50% 50% 10px 10px;
    background: radial-gradient(ellipse at 50% 60%, var(--gold) 0%, var(--gold-deep) 55%, rgba(201,154,18,0.15) 100%);
  }

  /* Card front: identity */
  .card-front { left: 550px; top: 450px; }
  .service-emblem {
    position: absolute;
    left: 32px;
    top: 92px;
    width: 42px;
    height: 50px;
    border-radius: 50%;
    background: radial-gradient(circle, var(--gold) 0%, var(--gold-deep) 80%);
  }
  .name-flourish {
    position: absolute;
    left: 174px;
    top: 92px;
    width: 126px;
    height: 5px;
    border-radius: 3px;
    background: linear-gradient(90deg, rgba(240,196,25,0) 0%, var(--gold) 40%, var(--gold) 60%, rgba(240,196,25,0) 100%);
  }
  .identity {
    position: absolute;
    left: 0;
    right: 0;
    top: 108px;
    text-align: center;
  }
  .person-name {
    font-family: var(--sans);
    font-weight: 400;
    font-size: 25px;
    line-height: 30px;
    color: var(--gold);
  }
  .role-title {
    margin-top: 4px;
    font-family: var(--serif);
    font-weight: 700;
    font-size: 12.5px;
    letter-spacing: 3px;
    color: var(--gold);
  }
  .slogan {
    position: absolute;
    right: 30px;
    top: 206px;
    font-family: var(--serif);
    font-weight: 700;
    font-size: 15px;
    color: var(--gold-muted);
  }
  .card-front .rule-upper { left: 10px; right: 10px; top: 232px; height: 2px; }
  .card-front .rule-lower { left: 10px; right: 10px; top: 272px; height: 2px; }
  .contact-row {
    position: absolute;
    left: 12px;
    right: 10px;
    top: 244px;
    display: flex;
    align-items: center;
    justify-content: space-between;
    font-size: 10.6px;
    white-space: nowrap;
  }
  .contact-item {
    display: flex;
    align-items: center;
    gap: 5px;
  }
  .contact-icon { width: 11px; height: 11px; flex: none; }
  .network-mark {
    width: 9px;
    height: 9px;
    background: var(--gold);
    flex: none;
  }
</style>
</head>
<body>
<main class="canvas">

  <section class="card card-back" aria-label="Business card back">
    <div class="rule rule-top"></div>
    <ul class="qualifications">
      <li><svg class="tick" viewBox="0 0 14 14"><path d="M2 7.5 L5.5 11 L12 3" fill="none" stroke="#f0c419" stroke-width="2.6" stroke-linecap="round" stroke-linejoin="round"/></svg>8 years military supply, logistics, &amp; administrative experience</li>
      <li><svg class="tick" viewBox="0 0 14 14"><path d="M2 7.5 L5.5 11 L12 3" fill="none" stroke="#f0c419" stroke-width="2.6" stroke-linecap="round" stroke-linejoin="round"/></svg>2 years intensive recruiting, marketing, and sales expertise</li>
      <li><svg class="tick" viewBox="0 0 14 14"><path d="M2 7.5 L5.5 11 L12 3" fill="none" stroke="#f0c419" stroke-width="2.6" stroke-linecap="round" stroke-linejoin="round"/></svg>Adept problem solving, planning and management skills</li>
      <li><svg class="tick" viewBox="0 0 14 14"><path d="M2 7.5 L5.5 11 L12 3" fill="none" stroke="#f0c419" stroke-width="2.6" stroke-linecap="round" stroke-linejoin="round"/></svg>5 Star, 5 Daimond, Luxury Hotels &amp; Hospitality Rooms &amp; Revenue</li>
    </ul>
    <div class="rule rule-bottom"></div>
    <div class="hotel-crest" role="img" aria-label="Gold illustration of five stars above a luxury hotel tower with palm trees and a row of diamonds"></div>
  </section>

  <section class="card card-front" aria-label="Business card front">
    <div class="service-emblem" role="img" aria-label="Small gold Lion, Compass, &amp; Rope emblem"></div>
    <div class="name-flourish" role="img" aria-label="Gold decorative flourish above the name"></div>
    <div class="identity">
      <h1 class="person-name">Corbin T. Pellman</h1>
      <p class="role-title">Luxury Hospitality</p>
    </div>
    <p class="slogan">My Experience = Our Success</p>
    <div class="rule rule-upper"></div>
    <div class="contact-row">
      <span class="contact-item">
        <svg class="contact-icon" viewBox="0 0 12 12"><path d="M2.6 1 L4.4 1 L5.2 3.4 L4 4.4 Q5 6.8 7.6 8 L8.6 6.8 L11 7.6 L11 9.4 Q10.6 11 9 11 Q1 10 1 2.6 Q1 1 2.6 1 Z" fill="#f0c419"/></svg>
        555-317-8846
      </span>
      <span class="contact-item">
        <svg class="contact-icon" viewBox="0 0 12 12"><rect x="0.8" y="2.2" width="10.4" height="7.6" fill="none" stroke="#f0c419" stroke-width="1.3"/><path d="M1 2.6 L6 6.6 L11 2.6" fill="none" stroke="#f0c419" stroke-width="1.3"/></svg>
        ridgefellow@mailvessel.example
      </span>
      <span class="contact-item">
        <span class="network-mark"></span>
        Net Roster /corbin-pellman-vet-civ
      </span>
    </div>
    <div class="rule rule-lower"></div>
  </section>

</main>
</body>
</html>
```